Whimsical Aquaculture Farm Packaging Logo

Aquaculture farm in Rhode Island growing hard shell clams (known locally as "quahogs") needs a fun/whimsical (but not silly) label to put on boxes for its "Yuletide Haul." The "Yuletide Haul" is actually candy to be given out to friends. The name of the farm is "Vessini Aquaculture Farm."

Boxes are roughly 8x10 so label should fit within those dimensions.

Requirements:
1) Include "Vessini Aquaculture Farm" on the label (it is OK to de-emphasize 'aquaculture' in the type).
2) Include "Yuletide Haul" (should be more prominent than #1)
3) Do NOT include the year.

Picture of a quahog attached.

Target Market(s)

Existing customers who know us and will get a laugh or chuckle from the playful "Yuletide Haul" candy.

Industry/Entity Type

Farm

Font styles to use
Serif
Decorative

Colors
33a6d7
85cae6
0892cd
0455a3
3176b5
85acd3

Requirements
Must have
• Should have blue in it (because aquaculture is farming in the ocean).
Should not have
• A date.

```html
<!DOCTYPE html>
<html lang="en">
<head>
<meta charset="utf-8">
<title>Vessini Aquaculture Farm – Yuletide Haul label</title>
<link rel="stylesheet" href="https://fonts.googleapis.com/css2?family=Rubik:wght@900&display=swap">
<style>
  :root {
    --page: #ffffff;
    --sky-light: #85cae6;
    --sky: #33a6d7;
    --ocean: #0892cd;
    --deep: #0455a3;
    --steel: #3176b5;
    --mist: #85acd3;
    --upper-top: #0d4c9c;
    --upper-bottom: #1a66b8;
    --navy: #24215f;
    --navy-glow: #2f3286;
    --band: #2b8fd4;
    --white: #ffffff;
  }
  html, body {
    margin: 0;
    width: 1200px;
    height: 1000px;
    overflow: hidden;
    background: var(--page);
  }
  .canvas { display: block; width: 1200px; height: 1000px; }
  .farm-name {
    font-family: "Rubik", sans-serif;
    font-weight: 900;
    fill: var(--white);
    text-anchor: middle;
  }
  .headline {
    font-family: "Rubik", sans-serif;
    font-weight: 900;
    fill: var(--sky);
    stroke: var(--white);
    stroke-width: 16;
    stroke-linejoin: round;
    paint-order: stroke fill;
    text-anchor: middle;
  }
</style>
</head>
<body>
<svg class="canvas" viewBox="0 0 1200 1000" xmlns="http://www.w3.org/2000/svg" aria-label="Yuletide Haul label for Vessini Aquaculture Farm">
  <defs>
    <clipPath id="label-clip"><rect x="300" y="92" width="634" height="792"/></clipPath>
    <linearGradient id="upper-fill" x1="0" y1="0" x2="0" y2="1">
      <stop offset="0" stop-color="var(--upper-top)"/>
      <stop offset="1" stop-color="var(--upper-bottom)"/>
    </linearGradient>
    <radialGradient id="navy-fill" cx="0.5" cy="0.5" r="0.6">
      <stop offset="0" stop-color="var(--navy-glow)"/>
      <stop offset="1" stop-color="var(--navy)"/>
    </radialGradient>
    <filter id="headline-shadow" x="-10%" y="-20%" width="120%" height="140%">
      <feDropShadow dx="0" dy="4" stdDeviation="4" flood-color="#0a0a30" flood-opacity="0.55"/>
    </filter>
  </defs>

  <g class="label" clip-path="url(#label-clip)">
    <g class="stripes">
      <rect x="300" y="92" width="40" height="792" fill="var(--sky-light)"/>
      <rect x="340" y="92" width="40" height="792" fill="var(--sky)"/>
      <rect x="380" y="92" width="60" height="792" fill="var(--ocean)"/>
      <rect x="440" y="92" width="60" height="792" fill="var(--deep)"/>
      <rect x="500" y="92" width="75" height="792" fill="var(--steel)"/>
      <rect x="575" y="92" width="40" height="792" fill="var(--mist)"/>
      <rect x="615" y="92" width="38" height="792" fill="var(--sky-light)"/>
      <rect x="653" y="92" width="45" height="792" fill="var(--sky)"/>
      <rect x="698" y="92" width="62" height="792" fill="var(--ocean)"/>
      <rect x="760" y="92" width="52" height="792" fill="var(--deep)"/>
      <rect x="812" y="92" width="78" height="792" fill="var(--steel)"/>
      <rect x="890" y="92" width="44" height="792" fill="var(--mist)"/>
    </g>

    <path class="upper-panel" role="img" aria-label="Winter swirl and snowflake pattern"
          d="M300,155 H934 V440 Q617,405 300,440 Z" fill="url(#upper-fill)"/>
    <path class="upper-band" d="M300,428 Q617,392 934,428 V472 Q617,438 300,472 Z" fill="var(--band)"/>
    <path class="navy-panel" role="img" aria-label="Winter swirl and snowflake pattern"
          d="M300,465 Q617,432 934,465 V772 Q617,738 300,772 Z" fill="url(#navy-fill)"/>
    <path class="lower-band" d="M300,752 Q617,720 934,752 V790 Q617,758 300,790 Z" fill="var(--sky)" opacity="0.85"/>
  </g>

  <g class="farm-name">
    <text x="617" y="285" font-size="72" textLength="330" lengthAdjust="spacingAndGlyphs">VESSINI</text>
    <text x="617" y="338" font-size="30" textLength="330" lengthAdjust="spacingAndGlyphs">AQUACULTURE FARM</text>
  </g>

  <g class="headline" filter="url(#headline-shadow)">
    <text x="630" y="618" font-size="118" textLength="540" lengthAdjust="spacingAndGlyphs">YULETIDE</text>
    <text x="632" y="718" font-size="104" textLength="240" lengthAdjust="spacingAndGlyphs">HAUL</text>
  </g>
</svg>
</body>
</html>
```